Glenvora pond linings website template

We need a template for our new website. Glenvora is currently marketed through www.sheetvale.com.au, and we are moving the pond/dam linings to a dedicated site www.glenvora.com.au

The site is essentially brochureware. The content (less landing page & photo gallery) is on the new site to give you a better idea of what we do. We are also on Facebook.com/glenvora

We are looking for a template/style which we can adapt to the different sections of the site as required. We also get a lot of phone/tablet visitors so an alternative mobile layout would be a bonus, but by no means required.

I am proficient in HTML/CSS & javascript so can code most designs thrown at me.

Any icons or interface fonts should be freely available web fonts where possible.

Target Market(s)

We are targeting both landscape professionals (design & construction) as well as the DIY market for ponds/wateragrdens.

Industry/Entity Type

Moving

Requirements
Must have
• We need a design (preferably layered PSD or AI) as basis for our overall site look and feel. Fonts/iconography/layout are where we are lacking. We can do the HTML/CSS/JS/PHP internally.
Nice to have
• A style guide either in file or separate would be nice.
Layers with effect (i.e.. :hover, CSS3 transition endpoints, etc)

```html
<!DOCTYPE html>
<html lang="en">
<head>
<meta charset="utf-8">
<title>Glenvora – Pond Linings</title>
<link href="https://fonts.googleapis.com/css2?family=Source+Sans+3:wght@400;600;700&display=swap" rel="stylesheet">
<style>
:root{
  --green-dark:#00774a;
  --green-lime:#6a9a2e;
  --green-deep:#005c39;
  --nav-grey:#55585b;
  --text-grey:#7a7a7a;
  --border:#dcdcdc;
  --white:#ffffff;
}
*{margin:0;padding:0;box-sizing:border-box}
html,body{width:1200px;height:1084px;overflow:hidden;background:var(--white);font-family:"Source Sans 3",sans-serif}
.page{position:relative;width:1200px;height:1084px}
.abs{position:absolute}

.brand{left:181px;top:30px;display:flex;align-items:center;gap:10px;color:var(--green-dark);font-size:30px;font-weight:600;letter-spacing:1px}
.brand-mark{width:22px;height:22px;background:var(--green-lime)}

.phone{left:626px;top:44px;display:flex;align-items:center;gap:8px;color:var(--green-dark);font-size:17px}
.search{left:783px;top:45px;width:236px;height:24px;border:1px solid #ccc;border-radius:2px;background:linear-gradient(#f4f4f4,#fff);font-size:8px;color:#888;padding:7px 0 0 11px}
.search svg{position:absolute;right:8px;top:5px}

.nav{left:0;top:103px;width:1200px;height:39px;background:linear-gradient(#64676a,var(--nav-grey))}
.nav a{position:absolute;top:0;height:39px;line-height:39px;color:var(--white);font-size:11px;text-decoration:none}
.nav a.active{background:var(--green-lime);width:79px;text-align:center}

.hero-photo{left:181px;top:163px;width:583px;height:345px;background:linear-gradient(180deg,#a9c9e0 0%,#d9c7a2 40%,#9a7c58 62%,#3e4a45 100%)}
.slider-dots{left:711px;top:491px;display:flex;gap:2px}
.slider-dots span{width:8px;height:8px;background:#b8c6c9}
.slider-dots span:first-child{background:var(--white)}
.hero-panel{left:764px;top:163px;width:257px;height:345px;background:var(--green-dark);color:var(--white);padding:0 0 0 25px}
.hero-panel .fold{position:absolute;right:0;top:0}
.hero-panel .kicker{margin-top:32px;font-size:17px;font-weight:600}
.hero-panel h1{font-size:34px;font-weight:700;line-height:1;margin-top:8px}
.hero-panel p{font-size:9.5px;line-height:15.4px;margin:13px 12px 0 3px}
.hero-panel p + p{margin-top:15px}
.btn{display:inline-block;background:var(--green-lime);color:var(--white);font-size:9.5px;text-align:center;text-decoration:none;border-radius:2px}
.hero-btn{position:absolute;left:30px;top:286px;width:159px;height:33px;line-height:33px}

.feature{top:534px;width:264px}
.feature h2{color:var(--green-dark);font-size:12px;font-weight:600;height:27px}
.feature .photo{height:138px}
.feature p{margin-top:19px;padding:0 2px;font-size:9.5px;line-height:15.4px;color:var(--text-grey);text-align:justify;height:65px}
.feature .btn{width:91px;height:24px;line-height:24px}

.gallery-title{left:182px;top:843px;color:var(--green-dark);font-size:12px;font-weight:600}
.arrows{left:983px;top:844px;display:flex;gap:3px}
.arrows span{width:17px;height:17px;background:#e2e2e2;display:flex;align-items:center;justify-content:center}
.thumb{top:873px;width:199px;height:110px;border:1px solid var(--border);padding:6px}
.thumb div{width:100%;height:100%}

.footer{left:0;top:1010px;width:1200px;height:74px;background:var(--green-lime);color:var(--white)}
.footer-links{position:absolute;left:183px;top:24px;font-size:8px;font-weight:600;display:flex;gap:0}
.footer-links span.sep{margin:0 12px}
.copyright{position:absolute;left:183px;top:44px;font-size:7.5px;font-weight:600}
.follow{position:absolute;left:824px;top:25px;display:flex;align-items:center;gap:4px;font-size:7.5px;font-weight:600}
.follow i{width:25px;height:25px;border-radius:50%;background:var(--green-deep);display:block}
</style>
</head>
<body>
<div class="page">

  <div class="abs brand"><span class="brand-mark"></span>GLENVORA</div>

  <div class="abs phone">
    <svg width="26" height="26" viewBox="0 0 24 24"><path fill="#9a9a9a" d="M6.6 10.8c1.4 2.8 3.8 5.1 6.6 6.6l2.2-2.2c.3-.3.7-.4 1-.2 1.1.4 2.3.6 3.6.6.6 0 1 .4 1 1V20c0 .6-.4 1-1 1C10.6 21 3 13.4 3 4c0-.6.4-1 1-1h3.5c.6 0 1 .4 1 1 0 1.3.2 2.5.6 3.6.1.3 0 .7-.2 1z"/></svg>
    1300 55 70 12
  </div>

  <div class="abs search">SEARCH :
    <svg width="14" height="14" viewBox="0 0 14 14"><circle cx="5.5" cy="5.5" r="4" fill="none" stroke="#b5b5b5" stroke-width="1.5"/><line x1="8.5" y1="8.5" x2="13" y2="13" stroke="#b5b5b5" stroke-width="2"/></svg>
  </div>

  <nav class="abs nav">
    <a class="active" style="left:180px" href="#">HOME</a>
    <a style="left:286px" href="#">ABOUT US</a>
    <a style="left:387px" href="#">HAPPENINGS</a>
    <a style="left:500px" href="#">GALLERY</a>
    <a style="left:594px" href="#">LINER STYLES</a>
    <a style="left:709px" href="#">PREPARATION</a>
    <a style="left:825px" href="#">INSTALLATION</a>
    <a style="left:943px" href="#">CONTACT US</a>
  </nav>

  <div class="abs hero-photo" role="img" aria-label="Backyard pond with a round timber deck beside a weatherboard house"></div>
  <div class="abs slider-dots"><span></span><span></span><span></span><span></span></div>

  <section class="abs hero-panel">
    <svg class="fold" width="26" height="26" viewBox="0 0 26 26"><polygon points="0,0 26,26 0,26" fill="var(--green-deep)"/><polygon points="0,0 26,0 26,26" fill="var(--white)"/></svg>
    <div class="kicker">Welcome to</div>
    <h1>GLENVORA</h1>
    <p>Why have one backyard garden when you can have two? This question was the inspiration for the latest creation from Tom Ardley Landscape Design. His design creates two distinctly different gardens next to each other with a common flow, and some very creative ideas.</p>
    <p>Toms designs include many small details which leave a finished result which can only be described as breathtaking. The first detail which is difficult to see unless you are directly.</p>
    <a class="btn hero-btn" href="#">CLICK HERE FOR MORE INFO</a>
  </section>

  <article class="abs feature" style="left:181px">
    <h2>TWO GARDENS IN ONE BACKYARD</h2>
    <div class="photo" role="img" aria-label="Waterfall garden with ferns and a small ladder" style="background:linear-gradient(135deg,#4f7a2c,#2f4a22 55%,#8aa7a3)"></div>
    <p>Why have one backyard garden when you can have two? This question was the inspiration for the latest creation from Tom Ardley Landscape Design. His design creates two distinctly different gardens</p>
    <a class="btn" href="#">READ MORE</a>
  </article>

  <article class="abs feature" style="left:472px">
    <h2>ABOUT US</h2>
    <div class="photo" role="img" aria-label="Team group at an awards evening holding framed certificates" style="background:linear-gradient(135deg,#3a2e28,#6b5648 50%,#2a2422)"></div>
    <p>Why have one backyard garden when you can have two? This question was the inspiration for the latest creation from Tom Ardley Landscape Design. His design creates two distinctly different gardens</p>
    <a class="btn" href="#">READ MORE</a>
  </article>

  <article class="abs feature" style="left:757px">
    <h2>PREPARATION</h2>
    <div class="photo" role="img" aria-label="Excavated pond site prepared for lining" style="background:linear-gradient(180deg,#8fb0c8 0%,#5b6a48 35%,#9b8a72 55%,#b7a78f 100%)"></div>
    <p>Why have one backyard garden when you can have two? This question was the inspiration for the latest creation from Tom Ardley Landscape Design. His design creates two distinctly different gardens</p>
    <a class="btn" href="#">READ MORE</a>
  </article>

  <div class="abs gallery-title">PHOTO GALLERY</div>
  <div class="abs arrows">
    <span><svg width="5" height="7"><polygon points="5,0 0,3.5 5,7" fill="#fff"/></svg></span>
    <span><svg width="5" height="7"><polygon points="0,0 5,3.5 0,7" fill="#fff"/></svg></span>
  </div>

  <div class="abs thumb" style="left:181px"><div role="img" aria-label="Still pond with a large rock" style="background:linear-gradient(135deg,#c8c2b4,#6e6a55 60%,#3f4333)"></div></div>
  <div class="abs thumb" style="left:394px"><div role="img" aria-label="Rust-coloured garden sculpture among ferns" style="background:linear-gradient(135deg,#6f8b5a,#a2472a 50%,#e8e4dc)"></div></div>
  <div class="abs thumb" style="left:608px"><div role="img" aria-label="Shallow stream with pebbles and grasses" style="background:linear-gradient(135deg,#7d7f62,#8a9e5a 55%,#4e7a2d)"></div></div>
  <div class="abs thumb" style="left:822px"><div role="img" aria-label="Water garden planting with tree ferns" style="background:linear-gradient(135deg,#55643f,#7e8f5b 50%,#3b4a2d)"></div></div>

  <footer class="abs footer">
    <div class="footer-links">
      <span>HOME</span><span class="sep">|</span>
      <span>ABOUT US</span><span class="sep">|</span>
      <span>HAPPENINGS</span><span class="sep">|</span>
      <span>GALLERY</span><span class="sep">|</span>
      <span>LINER STYLES</span><span class="sep">|</span>
      <span>PREPARATION</span><span class="sep">|</span>
      <span>INSTALLATION</span><span class="sep">|</span>
      <span>CONTACT US</span>
    </div>
    <div class="copyright">COPRIGHTS © 2013, GLENVORA. ALL RIGHTS RESERVED.</div>
    <div class="follow">FOLLOW US :<i></i><i></i><i></i><i></i><i></i></div>
  </footer>

</div>
</body>
</html>
```